"Velmaro" sparkling beverage

Dear All!
I need a stick label (82*95 - front label, 82*65 - back label )design for а sparkling beverage, name is "Velmaro", 4 flavours: lemonade,duchess pear, estragon, original. Transparent glass bottles 0,5 liter (alumnium closure 28*15)/0,33 liter (crown cap), neck label should also be on the bottle 0,5 liter.
European style is welcomed
Do not send the disigns with a little changes several times, please!!!
Young people from 12-30 ages old

```html
<!DOCTYPE html>
<html lang="en">
<head>
<meta charset="utf-8">
<title>Velmaro – Label Range</title>
<link rel="stylesheet" href="https://fonts.googleapis.com/css2?family=Fredoka:wght@500;600&family=Dancing+Script:wght@500;600&display=swap">
<style>
  :root {
    --canvas: #ffffff;
    --label-paper: #ffffff;
    --label-edge: #ececec;
    --leaf-green: #6e9a3c;

    --lemon-brand: #e0a81c;
    --lemon-flavour: #7a9a3a;
    --lemon-tag: #8aa640;
    --lemon-art-a: #fbeb8a;
    --lemon-art-b: #f2c12a;
    --lemon-art-c: #e9a91a;

    --tarragon-brand: #9cc92a;
    --tarragon-flavour: #e2b614;
    --tarragon-tag: #d9b21f;
    --tarragon-art-a: #d9e8bd;
    --tarragon-art-b: #9bbf68;
    --tarragon-art-c: #5f8a34;

    --pear-brand: #e08a1c;
    --pear-flavour: #6f9a35;
    --pear-tag: #6f9a35;
    --pear-art-a: #f6d95a;
    --pear-art-b: #efb13a;
    --pear-art-c: #df7a24;
  }

  * { box-sizing: border-box; margin: 0; padding: 0; }

  html, body {
    width: 1200px;
    height: 1200px;
    overflow: hidden;
    background: var(--canvas);
  }

  .label-range {
    width: 1200px;
    height: 1200px;
    display: flex;
    justify-content: center;
    align-items: center;
    gap: 48px;
  }

  .front-label {
    position: relative;
    width: 330px;
    height: 484px;
    background: var(--label-paper);
    border: 1px solid var(--label-edge);
    display: flex;
    flex-direction: column;
    align-items: center;
    overflow: hidden;
  }

  .brand-mark {
    margin-top: 52px;
    width: 44px;
    height: 44px;
    border-radius: 50%;
    background: var(--leaf-green);
  }

  .brand-name {
    margin-top: 20px;
    font-family: "Fredoka", sans-serif;
    font-weight: 600;
    font-size: 64px;
    line-height: 1;
    letter-spacing: 0.5px;
    text-transform: uppercase;
  }

  .flavour-name {
    margin-top: 6px;
    font-family: "Fredoka", sans-serif;
    font-weight: 600;
    font-size: 30px;
    line-height: 1;
    letter-spacing: 1px;
    text-transform: uppercase;
  }

  .tagline {
    margin-top: 4px;
    font-family: "Dancing Script", cursive;
    font-weight: 500;
    font-size: 25px;
    line-height: 1.1;
  }

  .tagline--large { font-size: 32px; font-weight: 600; margin-top: 0; }

  .fruit-art {
    position: absolute;
    left: 0;
    bottom: 0;
    width: 100%;
    height: 200px;
  }

  .fruit-art--tall { height: 214px; }

  .front-label--lemon .brand-name { color: var(--lemon-brand); }
  .front-label--lemon .flavour-name { color: var(--lemon-flavour); }
  .front-label--lemon .tagline { color: var(--lemon-tag); }
  .front-label--lemon .fruit-art {
    background: linear-gradient(180deg, var(--label-paper) 0%, var(--lemon-art-a) 18%, var(--lemon-art-b) 60%, var(--lemon-art-c) 100%);
  }

  .front-label--tarragon .brand-name { color: var(--tarragon-brand); }
  .front-label--tarragon .flavour-name { color: var(--tarragon-flavour); }
  .front-label--tarragon .tagline { color: var(--tarragon-tag); }
  .front-label--tarragon .fruit-art {
    background: linear-gradient(180deg, var(--label-paper) 0%, var(--tarragon-art-a) 18%, var(--tarragon-art-b) 60%, var(--tarragon-art-c) 100%);
  }

  .front-label--pear .brand-name { color: var(--pear-brand); }
  .front-label--pear .flavour-name { color: var(--pear-flavour); font-size: 27px; }
  .front-label--pear .tagline { color: var(--pear-tag); }
  .front-label--pear .fruit-art {
    background: linear-gradient(180deg, var(--label-paper) 0%, var(--pear-art-a) 16%, var(--pear-art-b) 55%, var(--pear-art-c) 100%);
  }
</style>
</head>
<body>
  <main class="label-range">
    <section class="front-label front-label--lemon">
      <span class="brand-mark"></span>
      <h1 class="brand-name">Velmaro</h1>
      <h2 class="flavour-name">Lemonade</h2>
      <p class="tagline">100% Real fruits</p>
      <div class="fruit-art" role="img" aria-label="Watercolour illustration of sliced lemons with juice splashes"></div>
    </section>

    <section class="front-label front-label--tarragon">
      <span class="brand-mark"></span>
      <h1 class="brand-name">Velmaro</h1>
      <h2 class="flavour-name">Estragon</h2>
      <p class="tagline">100% Real fruits</p>
      <div class="fruit-art" role="img" aria-label="Watercolour illustration of tarragon sprigs"></div>
    </section>

    <section class="front-label front-label--pear">
      <span class="brand-mark"></span>
      <h1 class="brand-name">Velmaro</h1>
      <h2 class="flavour-name">Duchess Pear</h2>
      <p class="tagline tagline--large">Sparkling</p>
      <div class="fruit-art fruit-art--tall" role="img" aria-label="Watercolour illustration of ripe yellow and orange pears with leaves"></div>
    </section>
  </main>
</body>
</html>
```